Remodel Flyer for realtors

"K" Tandem Builders

4"x 9" rack card front and back

www.BrindleyRenovator.com

555-318-4762

Let us fix what your home inspector finds!

Send us your inspection summary.

We are a licensed and Insured contractor.
CRC4871093

Serving
Marion County and The Heronfield

This flyer will sit in realtor offices for realtors to give to there buyers and sellers.

Target Market(s)

Realtors

Industry/Entity Type

Construction

Colors

Designer to choose colors to be used in the design.

```html
<!DOCTYPE html>
<html lang="en">
<head>
<meta charset="utf-8">
<title>K Tandem Builders – Rack Card Front and Back</title>
<link rel="stylesheet" href="https://fonts.googleapis.com/css2?family=Oswald:wght@400;500&family=Open+Sans:wght@400;600;700&family=Montserrat:wght@700&display=swap">
<style>
  :root {
    --stage: #0d3a5e;
    --stage-dark: #062338;
    --paper: #ffffff;
    --orange: #f39200;
    --ink: #2b2b2b;
    --body: #4a4a4a;
    --black-panel: #0c0c0c;
    --white: #ffffff;
  }
  * { box-sizing: border-box; margin: 0; padding: 0; }
  html, body { width: 833px; height: 1200px; overflow: hidden; }
  body {
    background: radial-gradient(ellipse at 50% 45%, var(--stage) 0%, var(--stage-dark) 100%);
    position: relative;
    font-family: "Open Sans", sans-serif;
  }
  .rack-card {
    position: absolute;
    top: 195px;
    width: 360px;
    height: 810px;
    background: var(--paper);
    overflow: hidden;
    box-shadow: 0 10px 30px rgba(0,0,0,.35);
  }
  .rack-card--front { left: 36px; }
  .rack-card--back { left: 437px; }
  .abs { position: absolute; }

  .brand { text-align: center; }
  .brand__mark { width: 42px; height: 42px; background: var(--orange); margin: 0 auto 10px; }
  .brand__name {
    font-family: "Oswald", sans-serif; font-weight: 500; color: var(--ink);
    font-size: 15px; letter-spacing: 2px; line-height: 1.1; text-transform: uppercase;
  }
  .brand__sub { font-size: 8px; letter-spacing: 6px; }

  .photo { position: absolute; }
  .photo--framed { border: 3px solid var(--white); }

  .heading {
    font-family: "Oswald", sans-serif; font-weight: 500; color: var(--ink);
    text-transform: uppercase; line-height: 1;
  }
  .tagline {
    font-family: "Oswald", sans-serif; font-weight: 500; color: var(--orange);
    font-size: 11px; text-transform: uppercase; letter-spacing: .4px; line-height: 1.2;
  }
  .copy { color: var(--body); font-size: 7.4px; line-height: 1.5; }
  .copy--center { text-align: center; }
  .copy--justify { text-align: justify; }
  .copy p + p { margin-top: 3px; }
  .copy strong { color: var(--ink); font-weight: 700; }

  .credentials {
    border-left: 3px solid var(--orange);
    padding-left: 7px;
    color: var(--body); font-size: 7.4px; line-height: 1.5;
  }
  .credentials strong { color: var(--ink); font-weight: 700; }

  .service-list {
    background: var(--black-panel);
    display: flex; flex-direction: column; justify-content: center; align-items: center;
    gap: 4px;
  }
  .service-list li {
    list-style: none; font-family: "Oswald", sans-serif; font-size: 10px;
    color: var(--orange); text-transform: uppercase; display: flex; align-items: center; gap: 4px;
  }
  .service-list svg { width: 8px; height: 8px; }

  .contact-band { position: absolute; left: 0; right: 0; bottom: 0; background: var(--orange); }
  .contact-label {
    font-family: "Oswald", sans-serif; font-size: 11.5px; color: var(--ink);
    text-transform: uppercase; font-weight: 500;
  }
  .contact-phone {
    font-family: "Montserrat", sans-serif; font-weight: 700; color: var(--white);
    display: flex; align-items: center; gap: 5px;
  }
  .contact-phone svg { width: 14px; height: 14px; }
  .contact-line {
    font-family: "Open Sans", sans-serif; font-weight: 700; color: var(--ink);
    font-size: 6.2px; line-height: 1.35; display: flex; gap: 4px; align-items: flex-start;
  }
  .contact-line svg { width: 7px; height: 7px; flex: none; margin-top: 1px; }
</style>
</head>
<body>

<!-- Front -->
<section class="rack-card rack-card--front">
  <div class="brand abs" style="left:0;right:0;top:20px;">
    <div class="brand__mark"></div>
    <div class="brand__name">K Tandem<br><span class="brand__sub">Builders</span></div>
  </div>

  <div class="photo" role="img" aria-label="Bright living room with fireplace, sofas and hardwood floor"
       style="left:0;top:122px;width:360px;height:230px;background:linear-gradient(160deg,#e7dcc7 0%,#c79a5e 45%,#b4581c 80%,#8a3a12 100%);"></div>

  <h1 class="heading abs" style="left:0;right:0;top:362px;text-align:center;font-size:20px;">Welcome!</h1>
  <div class="tagline abs" style="left:0;right:0;top:388px;text-align:center;">Let us fix what your home inspector finds!</div>
  <div class="copy copy--center abs" style="left:36px;width:288px;top:405px;">
    <p>Whether it’s getting your home remodeled or fixing damage that’s been done to your home, we’re here to help you every step of the way.</p>
    <p>“K” Tandem Builders has been around since 1976, so we really mean it when we say we’re here to help you. <strong>Send us your inspection summary.</strong></p>
  </div>

  <div class="photo" role="img" aria-label="Open-plan lounge with spiral staircase"
       style="left:12px;top:478px;width:226px;height:126px;background:linear-gradient(150deg,#f1ece3 0%,#d8c6a8 55%,#9c7a55 100%);"></div>

  <ul class="service-list abs" style="left:248px;top:478px;width:100px;height:126px;">
    <li>Kitchens <svg viewBox="0 0 10 10"><rect x=".5" y=".5" width="9" height="9" fill="none" stroke="#fff"/><path d="M2 5l2 2 4-5" fill="none" stroke="#fff" stroke-width="1.3"/></svg></li>
    <li>Bathrooms <svg viewBox="0 0 10 10"><rect x=".5" y=".5" width="9" height="9" fill="none" stroke="#fff"/><path d="M2 5l2 2 4-5" fill="none" stroke="#fff" stroke-width="1.3"/></svg></li>
    <li>Additions <svg viewBox="0 0 10 10"><rect x=".5" y=".5" width="9" height="9" fill="none" stroke="#fff"/><path d="M2 5l2 2 4-5" fill="none" stroke="#fff" stroke-width="1.3"/></svg></li>
    <li>Whole Homes <svg viewBox="0 0 10 10"><rect x=".5" y=".5" width="9" height="9" fill="none" stroke="#fff"/><path d="M2 5l2 2 4-5" fill="none" stroke="#fff" stroke-width="1.3"/></svg></li>
  </ul>

  <div class="contact-band" style="height:105px;"></div>

  <div class="photo" role="img" aria-label="Dark kitchen island with pendant lights"
       style="left:12px;top:614px;width:156px;height:132px;background:linear-gradient(160deg,#d9d4cb 0%,#4a3f37 45%,#1d1a18 100%);"></div>
  <div class="photo" role="img" aria-label="Light bedroom with large windows"
       style="left:180px;top:614px;width:168px;height:132px;background:linear-gradient(160deg,#f4efe5 0%,#cfc3ab 55%,#8d8f86 100%);"></div>

  <div class="contact-label abs" style="left:10px;top:754px;">Contact Us</div>
  <div class="contact-phone abs" style="left:10px;top:772px;font-size:15px;">
    <svg viewBox="0 0 14 14"><rect width="14" height="14" rx="2" fill="#fff"/><path d="M4 3l2 0 .6 2.3-1.2.8a6 6 0 0 0 2.5 2.5l.8-1.2L11 8v2c0 .6-.5 1-1 1A7 7 0 0 1 3 4c0-.5.4-1 1-1z" fill="#f39200"/></svg>
    555-318-4762
  </div>
  <div class="contact-line abs" style="left:212px;top:756px;width:140px;">
    <svg viewBox="0 0 8 8"><path d="M4 0a3 3 0 0 1 3 3c0 2-3 5-3 5S1 5 1 3a3 3 0 0 1 3-3z" fill="#fff"/><circle cx="4" cy="3" r="1" fill="#f39200"/></svg>
    <span>214 Larkspur Ln, Brindley, Florida 30000,<br>United States</span>
  </div>
  <div class="contact-line abs" style="left:212px;top:780px;">
    <svg viewBox="0 0 8 8"><circle cx="4" cy="4" r="3.5" fill="none" stroke="#fff"/><path d="M.5 4h7M4 .5c-2 2-2 5 0 7M4 .5c2 2 2 5 0 7" fill="none" stroke="#fff" stroke-width=".7"/></svg>
    <span>www.BrindleyRenovator.com</span>
  </div>
</section>

<!-- Back -->
<section class="rack-card rack-card--back">
  <div class="photo" role="img" aria-label="Open-plan lounge with spiral staircase and tall windows"
       style="left:10px;top:18px;width:340px;height:136px;background:linear-gradient(150deg,#f3efe7 0%,#dccab0 50%,#9a7550 100%);"></div>
  <div class="photo" role="img" aria-label="Dark kitchen island with bar stools and pendant lights"
       style="left:10px;top:164px;width:160px;height:226px;background:linear-gradient(170deg,#dcd8d0 0%,#4b433c 45%,#1c1a18 100%);"></div>
  <div class="photo" role="img" aria-label="Light bedroom with ceiling lamp"
       style="left:180px;top:164px;width:170px;height:136px;background:linear-gradient(160deg,#f2ede3 0%,#d2c6ad 55%,#8f8c80 100%);"></div>

  <div class="brand abs" style="left:190px;width:160px;top:318px;">
    <div class="brand__mark"></div>
    <div class="brand__name">K Tandem<br><span class="brand__sub">Builders</span></div>
  </div>

  <h2 class="heading abs" style="left:20px;top:424px;font-size:18px;">Our Services</h2>
  <div class="abs" style="left:20px;top:447px;font-size:7.5px;font-weight:700;color:var(--ink);">Residential or Commercial</div>
  <div class="copy copy--justify abs" style="left:20px;top:462px;width:174px;">
    <p>We’ve got all your needs covered: from residential remodels, to commercial damage repairs and everything in between. Don’t hesitate to ask us a question or inquire as to why a certain process has to take place. All of our staff are friendly and knowledgeable because we know what it’s like to be in your shoes. We want you to know just how special you and your project are to us, so we do our very best to ensure that you and your needs always come first. We even have a complimentary estimate where we’ll come out to you!</p>
  </div>

  <h2 class="heading abs" style="left:20px;top:600px;font-size:18px;">Our Promise</h2>
  <div class="copy copy--justify abs" style="left:20px;top:624px;width:174px;">
    <p>Our work is good. We promise. And behind that promise, we want you to know that we back our work with a satisfaction guarantee. We won’t stop working until you like what we’ve done.</p>
  </div>

  <div class="credentials abs" style="left:20px;top:682px;width:174px;">
    <strong>Licensed &amp; Insured Contractor · CRC4871093</strong><br>
    Serving Marion County and The Heronfield
  </div>

  <div class="contact-band" style="height:82px;"></div>

  <div class="photo" role="img" aria-label="White kitchen counter with kettle and microwave"
       style="left:206px;top:422px;width:134px;height:165px;background:linear-gradient(170deg,#f2f1ee 0%,#cfcac2 55%,#4d4943 100%);"></div>
  <div class="photo photo--framed" role="img" aria-label="Modern living corner with floor lamp and large windows"
       style="left:203px;top:596px;width:140px;height:164px;background:linear-gradient(160deg,#e9e8e4 0%,#9d9a94 50%,#3f3b37 100%);"></div>

  <div class="contact-label abs" style="left:20px;top:740px;">Contact Us</div>
  <div class="contact-phone abs" style="left:20px;top:758px;font-size:12px;">
    <svg viewBox="0 0 14 14" style="width:11px;height:11px;"><rect width="14" height="14" rx="2" fill="#fff"/><path d="M4 3l2 0 .6 2.3-1.2.8a6 6 0 0 0 2.5 2.5l.8-1.2L11 8v2c0 .6-.5 1-1 1A7 7 0 0 1 3 4c0-.5.4-1 1-1z" fill="#f39200"/></svg>
    555-318-4762
  </div>
  <div class="contact-line abs" style="left:20px;top:779px;width:160px;">
    <svg viewBox="0 0 8 8"><path d="M4 0a3 3 0 0 1 3 3c0 2-3 5-3 5S1 5 1 3a3 3 0 0 1 3-3z" fill="#fff"/><circle cx="4" cy="3" r="1" fill="#f39200"/></svg>
    <span>214 Larkspur Ln, Brindley, Florida 30000,<br>United States</span>
  </div>
  <div class="contact-line abs" style="left:205px;top:780px;">
    <svg viewBox="0 0 8 8"><circle cx="4" cy="4" r="3.5" fill="none" stroke="#fff"/><path d="M.5 4h7M4 .5c-2 2-2 5 0 7M4 .5c2 2 2 5 0 7" fill="none" stroke="#fff" stroke-width=".7"/></svg>
    <span>www.BrindleyRenovator.com</span>
  </div>
</section>

</body>
</html>
```